Business Consulting Business Card

professional business card with basic information (1) First and Last name (2) email address, (3) phone number, (4) website.

```html
<!DOCTYPE html>
<html lang="en">
<head>
<meta charset="utf-8">
<title>Cove Ridge Business Card</title>
<link rel="stylesheet" href="https://fonts.googleapis.com/css2?family=Montserrat:wght@300;400;500&display=swap">
<style>
  :root {
    --backdrop: #2b2b2d;
    --card: #0b3046;
    --card-light: #13405a;
    --accent: #2a78a8;
    --accent-soft: #1d5f88;
    --emboss: #0f3a54;
    --divider: #2a5773;
  }
  * { box-sizing: border-box; margin: 0; padding: 0; }
  html, body {
    width: 1200px; height: 900px; overflow: hidden;
    background: var(--backdrop);
    font-family: "Montserrat", sans-serif;
  }
  .canvas {
    position: relative; width: 1200px; height: 900px;
  }
  .card {
    position: absolute; left: 250px; width: 700px; height: 400px;
    border-radius: 22px;
    background: linear-gradient(120deg, var(--card) 0%, var(--card) 45%, var(--card-light) 75%, var(--card) 100%);
    box-shadow: 0 12px 30px rgba(0,0,0,0.45);
  }
  .card--front { top: 35px; }
  .card--back { top: 465px; background: var(--card); }

  .front-brand {
    position: absolute; left: 0; right: 0; top: 120px;
    display: flex; flex-direction: column; align-items: center; gap: 30px;
  }
  .brand-dot {
    width: 70px; height: 70px; border-radius: 50%;
    background: var(--accent-soft);
  }
  .brand-name {
    font-weight: 300; font-size: 44px; letter-spacing: 12px;
    color: var(--accent); text-transform: uppercase;
  }

  .back-mark {
    position: absolute; left: 95px; top: 115px;
    width: 150px; height: 150px; border-radius: 50%;
    background: var(--emboss);
    box-shadow: inset 2px 2px 4px rgba(0,0,0,0.35), inset -1px -1px 2px rgba(80,140,180,0.15);
  }
  .back-divider {
    position: absolute; left: 300px; top: 85px;
    width: 1px; height: 210px; background: var(--divider);
  }
  .contact {
    position: absolute; left: 335px; top: 110px; color: var(--accent);
  }
  .contact-name {
    font-weight: 500; font-size: 24px; letter-spacing: 2px; text-transform: uppercase;
  }
  .contact-role {
    font-weight: 400; font-size: 16px; color: var(--accent-soft); margin-top: 2px;
  }
  .contact-list { list-style: none; margin-top: 26px; }
  .contact-list li {
    display: flex; align-items: center; gap: 14px;
    font-size: 20px; font-weight: 400; color: var(--accent-soft);
    letter-spacing: 0.5px; margin-bottom: 8px;
  }
  .contact-list svg { width: 14px; height: 14px; flex: none; }
</style>
</head>
<body>
<main class="canvas">
  <section class="card card--front">
    <div class="front-brand">
      <span class="brand-dot"></span>
      <span class="brand-name">Cove Ridge</span>
    </div>
  </section>

  <section class="card card--back">
    <span class="back-mark"></span>
    <span class="back-divider"></span>
    <div class="contact">
      <div class="contact-name">Mark Ellison</div>
      <div class="contact-role">Director</div>
      <ul class="contact-list">
        <li>
          <svg viewBox="0 0 14 14" fill="none" stroke="#1d5f88" stroke-width="1.3"><path d="M3 1.5l2 2.5-1.2 1.4a8 8 0 0 0 4.8 4.8L10 9l2.5 2-1.2 1.7C6 12.5 1.5 8 1.3 2.7z"/></svg>
          (555) 210-4830
        </li>
        <li>
          <svg viewBox="0 0 14 14" fill="none" stroke="#1d5f88" stroke-width="1.3"><rect x="1" y="3" width="12" height="8"/><path d="M1 3l6 4.5L13 3"/></svg>
          hello@coveridge.com
        </li>
        <li>
          <svg viewBox="0 0 14 14" fill="none" stroke="#1d5f88" stroke-width="1.2"><circle cx="7" cy="7" r="5.8"/><ellipse cx="7" cy="7" rx="2.6" ry="5.8"/><path d="M1.2 7h11.6"/></svg>
          www.coveridge.com
        </li>
      </ul>
    </div>
  </section>
</main>
</body>
</html>
```